Flyer für IT-Dienstleistungen für Privatpersonen
Zielgruppe
IT-Dienstleistungen für Privatpersonen vorwiegened Senioren
Aufgabenstellung
Verwendet werden soll ein DIN A6 Zickzackfalz, Falz Längsseite, Bund Rechts, 6-8Seiten, Matt, Beschnittzugabe 1mm, Sicherheitsabstand 4mm, Farblich und Designtechnisch passend zur Webseite.
Die Textformatierung darf angepasst werden

```html
<!DOCTYPE html>
<html lang="de">
<head>
<meta charset="utf-8">
<title>Netzwacht – Flyer</title>
<link href="https://fonts.googleapis.com/css2?family=Montserrat:wght@500;600&family=Open+Sans:wght@400;600;700&display=swap" rel="stylesheet">
<style>
  :root{
    --bg-dark:#0d1b12;
    --bg-mid:#13291a;
    --green:#5dbb46;
    --green-deep:#2f8a3a;
    --green-glow:#3c9a46;
    --white:#ffffff;
    --text:#f2f5f2;
    --paper:#ffffff;
  }
  *{margin:0;padding:0;box-sizing:border-box}
  html,body{width:1145px;height:1200px;overflow:hidden;background:var(--paper)}
  body{position:relative;font-family:"Open Sans",Arial,sans-serif;color:var(--text)}
  .sheet{position:absolute;left:0;width:1145px;background:radial-gradient(ellipse at 85% 10%,#1d3a25 0%,var(--bg-dark) 55%),var(--bg-dark);overflow:hidden}
  .sheet--outside{top:0;height:537px}
  .sheet--inside{top:662px;height:538px}
  .abs{position:absolute}
  .brand{display:flex;align-items:center;gap:8px;font-family:"Montserrat",sans-serif;font-weight:600;color:var(--white);letter-spacing:.5px}
  .brand__dot{width:14px;height:14px;border-radius:50%;border:2px solid var(--white)}
  .brand--small{left:92px;top:54px;font-size:19px}
  .brand--large{left:434px;top:59px;font-size:22px}
  .hero-ring{left:65px;top:121px;width:250px;height:250px;border-radius:50%;background:radial-gradient(circle,#1e5a2a 55%,var(--green-deep) 100%);box-shadow:0 0 30px rgba(60,154,70,.4)}
  .hero-photo{left:90px;top:146px;width:200px;height:204px;border-radius:50%;background:radial-gradient(circle at 40% 40%,#f4f6f7 0%,#d8dde2 70%,#b8c2c8 100%)}
  .tagline{left:65px;top:430px;width:268px;font-weight:700;font-size:15.5px;line-height:21px;text-align:justify;color:var(--white)}
  .tagline em{font-style:normal;font-weight:400;color:var(--green);font-size:22px}
  .intro{left:427px;top:138px;width:305px;font-size:14.5px;line-height:19px}
  .h-sub{font-family:"Montserrat",sans-serif;font-weight:500;color:var(--white)}
  .referral-title{left:427px;top:289px;font-size:19.5px}
  .ref-line{left:427px;width:300px;font-size:14px;line-height:12px}
  .ref-line .big{color:var(--green);font-size:21px}
  .box{border:3px solid var(--green-glow);border-radius:56px;background:linear-gradient(180deg,#10201a 0%,#0d1a12 100%);box-shadow:0 0 18px rgba(60,154,70,.55),inset 0 0 14px rgba(60,154,70,.25)}
  .box--why{left:796px;top:87px;width:303px;height:395px}
  .box--prices{left:787px;top:673px;width:339px;height:516px}
  .why-title{left:819px;top:138px;font-size:19.5px}
  .why-item{left:819px;width:275px;font-size:14px;line-height:19px}
  .hl{color:var(--green)}
  .contact{left:819px;font-size:14px;line-height:19px}
  .contact-mark{left:1005px;top:399px;width:46px;height:46px;border-radius:50%;border:2px solid var(--green-glow)}
  .col-title{font-family:"Montserrat",sans-serif;font-weight:500;font-size:19.5px;line-height:22px;color:var(--white)}
  .col-sub{color:var(--green);font-size:14px;line-height:19px}
  .col-text{font-size:14px;line-height:19px;color:var(--text)}
  .price-title{left:813px;top:714px;font-family:"Montserrat",sans-serif;font-weight:500;font-size:19.5px}
  .price-group{left:813px;font-family:"Montserrat",sans-serif;font-weight:600;font-size:19px;color:var(--white)}
  .price-row{left:813px;font-size:13.5px;line-height:18px;white-space:nowrap}
</style>
</head>
<body>

<section class="sheet sheet--outside">
  <div class="abs brand brand--small"><span class="brand__dot"></span>NETZWACHT</div>
  <div class="abs hero-ring"></div>
  <div class="abs hero-photo" role="img" aria-label="Foto: Hand tippt auf Laptop-Tastatur mit Netzwerk-Symbolen"></div>
  <p class="abs tagline">Ob Computer, Smartphone &amp; Tablet – mit uns haben Sie einen Partner an Ihrer Seite, der <em>ALLES</em> für Sie regelt<span class="hl">.</span></p>

  <div class="abs brand brand--large"><span class="brand__dot"></span>NETZWACHT</div>
  <p class="abs intro">Wir wissen, wie wichtig zuverlässige Technik für den Alltag ist – und wie herausfordernd sie manchmal sein kann. Deshalb bieten wir Ihnen verständliche, kostengünstige und schnelle Unterstützung, die genau auf Ihre Bedürfnisse zugeschnitten ist.</p>
  <h2 class="abs h-sub referral-title">Kunden werben Kunden</h2>
  <p class="abs ref-line" style="top:326px"><span class="big">15€ Guthaben,</span> wenn ein Erstgespräch</p>
  <p class="abs ref-line" style="top:342px">zustande kommt</p>
  <p class="abs ref-line" style="top:369px">zusätzlich <span class="big">45€</span> sobald mind 3Std.</p>
  <p class="abs ref-line" style="top:388px">abgenommen wurde</p>

  <div class="abs box box--why"></div>
  <h2 class="abs h-sub why-title">Warum wir?</h2>
  <p class="abs why-item" style="top:170px"><span class="hl">Ehrlich und transparent</span>: Sie zahlen nur das, was Sie wirklich brauchen.</p>
  <p class="abs why-item" style="top:223px"><span class="hl">Non-Profit</span>: Wir handeln bei Privatkunden ohne Gewinnerzielungsabsicht.</p>
  <p class="abs why-item" style="top:276px"><span class="hl">Verständlich</span>: Wir erklären Technik in einfachen Worten.</p>
  <p class="abs why-item" style="top:329px"><span class="hl">Vor Ort oder per Fernwartung:</span> Flexibel, wie Sie es wünschen.</p>
  <p class="abs contact" style="top:398px">+49(0)&nbsp; 4471&nbsp; 5520374</p>
  <p class="abs contact" style="top:419px">vertrieb@netzwacht.de</p>
  <div class="abs contact-mark"></div>
</section>

<section class="sheet sheet--inside">
  <!-- column 1 -->
  <h2 class="abs col-title" style="left:47px;top:46px">Wartung &amp; Optimierung<br>Damit alles reibungslos läuft</h2>
  <p class="abs col-sub" style="left:47px;top:98px">Dauerhafte Computer-Prüfung</p>
  <p class="abs col-text" style="left:47px;top:132px;width:320px">Ein stabiler und sicherer Computer spart Zeit und Nerven. Wir überprüfen Ihre Geräte jeden Monat, damit alles wie am Schnürchen läuft.</p>
  <p class="abs col-sub" style="left:47px;top:203px">Computer-Optimierung</p>
  <p class="abs col-text" style="left:47px;top:237px;width:300px">Ist Ihr Computer langsam geworden? Wir beschleunigen ihn und sorgen dafür, dass Programme schneller starten und alles wieder Spaß macht.</p>
  <p class="abs col-sub" style="left:47px;top:328px">(Neu)Installation und Optimierung</p>
  <p class="abs col-text" style="left:47px;top:362px;width:320px">Ein neuer Computer oder ein frisches Betriebssystem? Wir übernehmen die Einrichtung und passen alles genau nach Ihren Wünschen an.</p>

  <!-- column 2 -->
  <h2 class="abs col-title" style="left:416px;top:49px">Sicherheitslösungen - Ihr Schutz<br>im digitalen Alltag</h2>
  <p class="abs col-sub" style="left:417px;top:100px;font-family:'Montserrat',sans-serif;font-weight:600">Virenscanner</p>
  <p class="abs col-text" style="left:417px;top:132px;width:300px">Wir schützen Sie vor Viren, Betrug und schädlicher Software. Installation, Einrichtung und Lizenz sind inklusive – damit Sie sich keine Sorgen mehr machen müssen.</p>
  <h2 class="abs col-title" style="left:417px;top:214px;font-size:19.5px;line-height:20px">Mobile Geräte - Ihr Smartphone<br>oder Tablet perfekt eingerichtet</h2>
  <p class="abs col-sub" style="left:417px;top:265px">Ersteinrichtung und Datenübertragung</p>
  <p class="abs col-text" style="left:417px;top:297px;width:290px">Ein neues Smartphone oder Tablet kann kompliziert wirken. Wir richten Ihr Gerät ein, übertragen Ihre Daten und installieren alle wichtige Apps.</p>
  <p class="abs col-sub" style="left:417px;top:384px;width:320px">Individuelle Dienstleistungen – Für Ihre speziellen Wünsche</p>
  <p class="abs col-text" style="left:417px;top:430px;width:300px">Haben Sie ein Anliegen, das nicht auf unserer Liste steht? Kein Problem – wir helfen Ihnen mit allem rund um Computer und Technik.</p>

  <!-- column 3 -->
  <div class="abs box box--prices" style="top:11px"></div>
  <h2 class="abs h-sub price-title" style="top:52px">Kostenfreie Dienstleistungen</h2>
  <p class="abs price-row" style="top:92px"><span class="hl">Erstberatung und Analyse:</span> Kostenlos</p>
  <h3 class="abs price-group" style="top:113px">Wartung und Optimierung</h3>
  <p class="abs price-row" style="top:146px"><span class="hl">Computer-Prüfung:</span> 5 € pro Monat &amp; Gerät</p>
  <p class="abs price-row" style="top:172px"><span class="hl">Computer-Reinigung:</span> 49 €</p>
  <p class="abs price-row" style="top:199px"><span class="hl">Computer-Optimierung:</span> 49 €</p>
  <p class="abs price-row" style="top:226px;left:812px;font-size:13px"><span class="hl">Computer-(Neu)installation &amp;Optimierung:</span> 99 €</p>
  <h3 class="abs price-group" style="top:248px">Netzwerk und Internet</h3>
  <p class="abs price-row" style="top:280px"><span class="hl">WLAN-Optimierung</span> 79 €</p>
  <p class="abs price-row" style="top:307px"><span class="hl">Netzwerkdrucker einrichten:</span> 59 €</p>
  <h3 class="abs price-group" style="top:329px">Sicherheitslösungen</h3>
  <p class="abs price-row" style="top:360px"><span class="hl">Virenscanner:</span> 10 € pro Monat</p>
  <h3 class="abs price-group" style="top:383px">Mob Geräte</h3>
  <p class="abs price-row" style="top:415px"><span class="hl">Smartphone- oder Tablet-Ersteinrichtung:</span> 59 €</p>
  <h3 class="abs price-group" style="top:437px">Allgemeine Arbeiten</h3>
  <p class="abs price-row" style="top:468px"><span class="hl">Individuelle Dienstleistungen:</span> 60 € pro Stunde</p>
</section>

</body>
</html>
```